Warren P Holcomb New Business Card Design

I assist families or individuals with downsizing. When they need to sell estate items I manage the process. I may buy their items. I may place their items with auction houses or I may bring in a variety of experts to sell all of the items. We help clients sell a huge variety of items including art, jewelry, coins, watches, antiques, collectibles, etc.

Target Market(s)

Two markets...One market is the clients I serve which are usually seniors or their family. These are individuals that need to sell on item or a house full if they estate is being liquidated. The other market is those that refer clients to me. Real Estate professionals, active senior communities, trust and estate lawyers and financial advisors.

Industry/Entity Type

Business

Contact Information for Business Card

This is a new business so we do not have a logo. We may not need a logo. Feel free to visit our website at www.warrenpholcomb-example.com for more information on the service we provide. I am a private consultant so my name needs to be prominent. My name is my brand. We need the card to let people know how to contact us via phone, website and email. Easy to read. Many of our clients are elderly.

Font styles to use
Sans Serif

Requirements
Must have
• My name. Our contact information.
• Warren P Holcomb
• 555-218-7431 Office
• 555-362-9184 Cell
• info@warrenpholcomb-example.com
• www.warrenpholcomb-example.com

```html
<!DOCTYPE html>
<html lang="en">
<head>
<meta charset="utf-8">
<title>Warren P Holcomb – Business Card</title>
<link href="https://fonts.googleapis.com/css2?family=Oswald:wght@500;700&family=Quicksand:wght@500&display=swap" rel="stylesheet">
<style>
  :root {
    --page-bg: #e9e7e4;
    --card-dark: #3b332b;
    --banner-tan: #b3a28d;
    --ink-dark: #3a3129;
    --text-light: #f4efe8;
    --icon-tone: #cfc4b6;
    --wood-deep: #3a1f10;
    --wood-mid: #7a4520;
    --wood-warm: #a8642e;
    --portrait-light: #d9d4cc;
    --portrait-suit: #2b2b33;
  }
  * { margin: 0; padding: 0; box-sizing: border-box; }
  html, body { width: 1200px; height: 900px; overflow: hidden; }
  body {
    background: var(--page-bg);
    position: relative;
    font-family: "Quicksand", sans-serif;
  }
  .card {
    position: absolute;
    left: 250px;
    width: 700px;
    height: 400px;
    overflow: hidden;
    box-shadow: 0 8px 24px rgba(0,0,0,.25);
  }
  .card-front { top: 30px; }
  .card-back { top: 470px; background: var(--card-dark); }

  /* Front */
  .front-photo {
    position: absolute; inset: 0;
    background:
      linear-gradient(90deg, rgba(20,14,10,.75) 0%, rgba(20,14,10,.15) 40%, rgba(0,0,0,0) 100%),
      linear-gradient(160deg, var(--wood-warm) 0%, var(--wood-mid) 45%, var(--wood-deep) 100%);
  }
  .front-name {
    position: absolute;
    left: 200px; top: 150px;
    font-family: "Oswald", sans-serif;
    font-weight: 700;
    font-size: 48px;
    line-height: 1;
    color: #ffffff;
    letter-spacing: 1px;
    text-shadow: 0 2px 6px rgba(0,0,0,.6);
    text-transform: uppercase;
    white-space: nowrap;
  }
  .front-title {
    position: absolute;
    left: 203px; top: 210px;
    font-family: "Oswald", sans-serif;
    font-weight: 700;
    font-size: 16px;
    color: #ffffff;
    letter-spacing: .5px;
    text-shadow: 0 1px 4px rgba(0,0,0,.7);
    text-transform: uppercase;
    white-space: nowrap;
  }

  /* Back */
  .name-banner { position: absolute; left: 0; top: 150px; width: 420px; height: 110px; }
  .back-name {
    position: absolute;
    left: 36px; top: 166px;
    font-family: "Oswald", sans-serif;
    font-weight: 700;
    font-size: 42px;
    line-height: 1;
    color: var(--ink-dark);
    text-transform: uppercase;
    white-space: nowrap;
  }
  .back-title {
    position: absolute;
    left: 38px; top: 220px;
    font-family: "Oswald", sans-serif;
    font-weight: 700;
    font-size: 13px;
    color: var(--ink-dark);
    text-transform: uppercase;
    white-space: nowrap;
  }
  .portrait {
    position: absolute;
    left: 455px; top: 40px;
    width: 205px; height: 170px;
    background: linear-gradient(180deg, var(--portrait-light) 0%, #bdb5aa 55%, var(--portrait-suit) 100%);
  }
  .contact-list {
    position: absolute;
    left: 130px; top: 286px;
    list-style: none;
  }
  .contact-item {
    display: flex; align-items: center;
    gap: 14px;
    font-size: 16px;
    color: var(--text-light);
    height: 30px;
    white-space: nowrap;
  }
  .contact-sep { opacity: .6; margin: 0 4px; }
  .contact-icon { width: 16px; height: 16px; fill: var(--icon-tone); flex: none; }
</style>
</head>
<body>

<section class="card card-front">
  <div class="front-photo" role="img" aria-label="Photo of Warren P Holcomb standing with arms crossed before wooden bookshelves filled with books and collectibles"></div>
  <h1 class="front-name">Warren P Holcomb</h1>
  <p class="front-title">Collectible Asset Buyer, Broker &amp; Consultant</p>
</section>

<section class="card card-back">
  <svg class="name-banner" viewBox="0 0 420 110" aria-hidden="true">
    <polygon points="0,18 420,0 398,92 0,110" fill="var(--banner-tan)"/>
  </svg>
  <h2 class="back-name">Warren P Holcomb</h2>
  <p class="back-title">Collectable Asset Buyer, Broker &amp; Consultant</p>

  <div class="portrait" role="img" aria-label="Head-and-shoulders portrait of Warren P Holcomb in a dark suit and lilac tie"></div>

  <ul class="contact-list">
    <li class="contact-item">
      <svg class="contact-icon" viewBox="0 0 16 16" aria-hidden="true"><path d="M2 5c0-2 2-3 6-3s6 1 6 3v1h-3V4.5H5V6H2z M4 7h8l2 6H2z"/><circle cx="8" cy="10" r="1.6" fill="var(--card-dark)"/></svg>
      <span>555-218-7431 Office<span class="contact-sep">|</span>555-362-9184 Cell</span>
    </li>
    <li class="contact-item">
      <svg class="contact-icon" viewBox="0 0 16 16" aria-hidden="true"><path d="M15 1 1 7l5 2 2 6z"/></svg>
      <span>info@warrenpholcomb-example.com</span>
    </li>
    <li class="contact-item">
      <svg class="contact-icon" viewBox="0 0 16 16" aria-hidden="true"><circle cx="8" cy="8" r="7"/><path d="M1 8h14M8 1c-3 3-3 11 0 14M8 1c3 3 3 11 0 14" stroke="var(--card-dark)" stroke-width="1.2" fill="none"/></svg>
      <span>www.warrenpholcomb-example.com</span>
    </li>
  </ul>
</section>

</body>
</html>
```